Awesome law firm seeks great artwork for sign to be installed at local roller skating rink!!

We're a dynamic, law firm that does its work with a difference - we actually care about our clients and our fees are usually lower than most other firms.

We are installing a sign that's 78cm (height) x 158cm (width) to be printed on 3mm Aluminum Composite Panel and installed at a local roller skating rink in Kalamunda, Perth, Western Australia.

Graphics need to be provided in vector .eps (Encapsulated Post Script), .ai (Adobe Illustrator) or PDF format.

We have uploaded a copy of our Logo, which should feature on the sign (we usually have it on the top right of our stationery, but are happy to see other suggestions), together with our practice areas - Family Law, Wills and Estates, Building and Construction, Corporate and Commercial, Local Government, General legal (personal or business).

We don't have a 'slogan' for our firm, but for the roller skating rink sign, we're thinking of something like 'We roll with you", or something similar. Surprise us :)

Sign should also indicate that our team are local to "the Hills", which is how this area (the Kalamunda and surrounding areas of Perth) is known.

Main colors of the sign can include blue, white, black and red (more blue, white and black preferred).

The final design should communicate trust and expertise in law, but have a fun edge (the sign's at a roller skating rink after all and will be seen on every lap as it's in the rink).

The sign must include our website address www.pelbarnlegal.com (note this is still under construction in case you google us :)), our phone number 0491 607 238 and our main email address, which is admin@pelbarnlegal.com

Beyond this, we're happy to see any cool ideas for the design of our sign.

Target Market(s)

Local families and business owners at local roller skating rink

Industry/Entity Type

Legal services

Font styles to use
Serif
Other font styles liked:
• Designer to choose

Colors
0054AA
0677BA
7BADD7
CADEEF
E8F1F8
EB3D1F
EC4F4E
F09395
F8D3D4
FCEDEE

Requirements
Must have
• Logo, contact details, design as per description and can have the words "Get your skates on!"
Nice to have
• Awesome, striking, appealing design - easy to read as you're zooming past on your skates!
Should not have
• Any offensive, explicit, corny or suggestive words and preferably avoid cliché rhyming catch phrases, albeit we do want something fun that has a skating vibe

```html
<!DOCTYPE html>
<html lang="en">
<head>
<meta charset="utf-8">
<title>Pelbarn Legal – Rink Sign</title>
<link rel="stylesheet" href="https://fonts.googleapis.com/css2?family=Arimo:wght@400;700&display=swap">
<style>
  :root {
    --ink: #000000;
    --paper: #ffffff;
    --backdrop: #e9ecef;
    --brand-blue: #3f6fcf;
    --skate-red: #ec1c24;
    --text-dark: #111111;
  }
  * { margin: 0; padding: 0; box-sizing: border-box; }
  html, body { width: 1200px; height: 785px; overflow: hidden; }
  body {
    background: var(--backdrop);
    font-family: "Arimo", Arial, sans-serif;
    position: relative;
  }
  .sign {
    position: absolute;
    left: 40px; top: 116px;
    width: 1120px; height: 553px;
    background: var(--paper);
    display: flex;
    box-shadow: 0 6px 24px rgba(0,0,0,.15);
  }
  .sign__promo {
    position: relative;
    width: 590px; height: 100%;
    background: var(--ink);
    color: var(--paper);
  }
  .headline {
    position: absolute;
    left: 78px; top: 118px;
    line-height: 1;
  }
  .headline__lead {
    display: block;
    font-size: 58px;
    font-weight: 400;
    letter-spacing: -1px;
  }
  .headline__main {
    display: block;
    margin-top: 4px;
    font-size: 88px;
    letter-spacing: -1px;
    white-space: nowrap;
  }
  .headline__skates { color: var(--skate-red); font-weight: 700; }
  .headline__on { font-weight: 400; margin-left: 14px; }

  .practice-areas {
    position: absolute;
    left: 62px; top: 326px;
    padding-left: 22px;
    border-left: 5px solid var(--brand-blue);
    list-style: none;
  }
  .practice-areas li {
    font-size: 24px;
    line-height: 38px;
    text-transform: uppercase;
    letter-spacing: -0.3px;
    white-space: nowrap;
  }
  .practice-areas small {
    font-size: 14px;
    margin-left: 6px;
  }

  .sign__brand {
    position: relative;
    flex: 1;
  }
  .firm-name {
    position: absolute;
    left: 80px; top: 98px;
    color: var(--brand-blue);
    font-size: 66px;
    font-weight: 400;
    line-height: 1.12;
    letter-spacing: 4px;
    text-transform: uppercase;
  }
  .contact {
    position: absolute;
    left: -20px; top: 330px;
    list-style: none;
  }
  .contact__row {
    display: flex;
    align-items: center;
    color: var(--text-dark);
  }
  .contact__row + .contact__row { margin-top: 24px; }
  .contact__icon {
    width: 58px; height: 58px;
    flex: none;
    border-radius: 50%;
    background: var(--brand-blue);
    display: flex; align-items: center; justify-content: center;
    margin-right: 24px;
  }
  .contact__phone {
    font-size: 56px;
    letter-spacing: 1px;
  }
  .contact__online {
    font-size: 29px;
    font-weight: 700;
    line-height: 1.3;
  }
</style>
</head>
<body>
  <section class="sign" aria-label="Pelbarn Legal rink sign">
    <div class="sign__promo">
      <h1 class="headline">
        <span class="headline__lead">Get your</span>
        <span class="headline__main"><span class="headline__skates">SKATES</span><span class="headline__on">on!</span></span>
      </h1>
      <ul class="practice-areas">
        <li>Family Law</li>
        <li>Wills and Estates</li>
        <li>Building and Construction</li>
        <li>Corporate and Commercial</li>
        <li>Local Government</li>
        <li>General Legal<small>(Personal or Business)</small></li>
      </ul>
    </div>
    <div class="sign__brand">
      <p class="firm-name">Pelbarn<br>Legal</p>
      <ul class="contact">
        <li class="contact__row">
          <span class="contact__icon">
            <svg width="30" height="30" viewBox="0 0 24 24" fill="none" stroke="#fff" stroke-width="1.8" stroke-linecap="round" stroke-linejoin="round" aria-hidden="true">
              <path d="M22 16.9v3a2 2 0 0 1-2.2 2 19.8 19.8 0 0 1-8.6-3.1 19.5 19.5 0 0 1-6-6A19.8 19.8 0 0 1 2.1 4.2 2 2 0 0 1 4.1 2h3a2 2 0 0 1 2 1.7c.1.9.4 1.9.7 2.8a2 2 0 0 1-.5 2.1L8 9.9a16 16 0 0 0 6 6l1.3-1.3a2 2 0 0 1 2.1-.4c.9.3 1.8.6 2.8.7a2 2 0 0 1 1.8 2z"/>
              <path d="M15 5a5 5 0 0 1 4 4M15 1a9 9 0 0 1 8 8"/>
            </svg>
          </span>
          <span class="contact__phone">0491 607 238</span>
        </li>
        <li class="contact__row">
          <span class="contact__icon">
            <svg width="32" height="32" viewBox="0 0 24 24" fill="none" stroke="#fff" stroke-width="1.8" aria-hidden="true">
              <circle cx="12" cy="12" r="10"/>
              <path d="M2 12h20M12 2a15 15 0 0 1 0 20M12 2a15 15 0 0 0 0 20"/>
            </svg>
          </span>
          <span class="contact__online">www.pelbarnlegal.com<br>admin@pelbarnlegal.com</span>
        </li>
      </ul>
    </div>
  </section>
</body>
</html>
```